Business Card for Consulting Company

I would need a business card for my consulting company - the company brand and logos are defined and shared as part of this project. The proposed design for the business card can be reused as inspiration for my email signature.

```html
<!DOCTYPE html>
<html lang="en">
<head>
<meta charset="utf-8">
<title>Corvane – Business Card</title>
<link rel="stylesheet" href="https://fonts.googleapis.com/css2?family=Open+Sans:wght@400;600;700&display=swap">
<style>
  :root {
    --teal: #14a9a6;
    --charcoal: #3b3b3d;
    --text: #4a4a4c;
    --card: #ffffff;
    --backdrop: #e6e7e9;
  }
  * { margin: 0; padding: 0; box-sizing: border-box; }
  html, body {
    width: 1200px; height: 907px; overflow: hidden;
    background: var(--backdrop);
    font-family: "Open Sans", Arial, sans-serif;
  }
  .stage {
    position: relative; width: 1200px; height: 907px;
    display: flex; align-items: center; justify-content: center; gap: 50px;
  }
  .card {
    position: relative; width: 525px; height: 300px;
    background: var(--card);
    box-shadow: 0 6px 18px rgba(0,0,0,.18);
  }
  .brand-name {
    font-weight: 600; color: var(--charcoal);
    letter-spacing: .5px; line-height: 1;
  }
  .brand-dot { display: block; border-radius: 50%; }

  /* Front */
  .front-brand {
    position: absolute; left: 40px; top: 34px;
    display: flex; flex-direction: column; align-items: flex-start; gap: 28px;
  }
  .front-brand .brand-dot {
    width: 176px; height: 176px; margin-left: 6px;
    background: var(--teal);
  }
  .front-brand .brand-name { font-size: 26px; }
  .holder {
    position: absolute; left: 300px; top: 42px;
  }
  .holder-name {
    font-size: 17px; font-weight: 700; color: var(--teal);
    text-transform: uppercase; letter-spacing: .3px; line-height: 1.3;
  }
  .holder-role { font-size: 12.5px; color: var(--text); margin-top: 2px; }
  .contacts {
    position: absolute; left: 300px; top: 150px;
    list-style: none; display: flex; flex-direction: column; gap: 8px;
  }
  .contact { display: flex; align-items: center; gap: 8px; font-size: 13px; color: var(--text); }
  .contact-icon {
    width: 15px; height: 15px; background: var(--teal); border-radius: 2px;
    display: flex; align-items: center; justify-content: center;
  }
  .contact-icon svg { width: 10px; height: 10px; }

  /* Back */
  .card-back { display: flex; align-items: center; justify-content: center; }
  .back-brand { display: flex; align-items: center; gap: 14px; }
  .back-brand .brand-dot { width: 34px; height: 34px; background: var(--teal); }
  .back-brand .brand-name { font-size: 40px; }
</style>
</head>
<body>
<main class="stage">
  <section class="card card-front" aria-label="Card front">
    <div class="front-brand">
      <span class="brand-dot"></span>
      <span class="brand-name">Corvane</span>
    </div>
    <div class="holder">
      <h1 class="holder-name">Lorin Vasseur</h1>
      <p class="holder-role">Founder &amp; CEO</p>
    </div>
    <ul class="contacts">
      <li class="contact">
        <span class="contact-icon"><svg viewBox="0 0 10 10"><path d="M2 1h2l1 2-1.2 1a5 5 0 0 0 2.2 2.2L7 5l2 1v2a1 1 0 0 1-1 1A7 7 0 0 1 1 2a1 1 0 0 1 1-1z" fill="#fff"/></svg></span>
        +41 79 000 12 34
      </li>
      <li class="contact">
        <span class="contact-icon"><svg viewBox="0 0 10 10"><rect x="1" y="2.5" width="8" height="5.5" fill="none" stroke="#fff" stroke-width="1"/><path d="M1 2.5l4 3 4-3" fill="none" stroke="#fff" stroke-width="1"/></svg></span>
        lorin.v@corvane.ch
      </li>
      <li class="contact">
        <span class="contact-icon"><svg viewBox="0 0 10 10"><circle cx="5" cy="5" r="3.8" fill="none" stroke="#fff" stroke-width="1"/><ellipse cx="5" cy="5" rx="1.6" ry="3.8" fill="none" stroke="#fff" stroke-width=".8"/><path d="M1.2 5h7.6" stroke="#fff" stroke-width=".8"/></svg></span>
        www.corvane.ch
      </li>
    </ul>
  </section>
  <section class="card card-back" aria-label="Card back">
    <div class="back-brand">
      <span class="brand-dot"></span>
      <span class="brand-name">Corvane</span>
    </div>
  </section>
</main>
</body>
</html>
```